New website for Pilates Studio

I need a new version of my website
http://brightcoreflow.biz/
I want an updated fresh look with an easier to read schedule that looks good on mobile phones as well as laptops.
Clean, simple, fresh and BOLD

Target Market(s)

All ages, genders and races

Coding

Number of Pages Required

Colors
9bcb3c

Requirements
Must have
• Photos that mostly use the real images from our studio. Browse our facebook page, website or ask me for high quality images

```html
<!DOCTYPE html>
<html lang="en">
<head>
<meta charset="utf-8">
<title>BrightCore Flow Pilates</title>
<link href="https://fonts.googleapis.com/css2?family=Lora:ital,wght@0,400;0,600;1,400&family=Open+Sans:wght@400;600&display=swap" rel="stylesheet">
<style>
:root{
  --green:#9bcb3c;
  --olive:#7f9a35;
  --ink:#4a4a40;
  --muted:#8a887a;
  --paper:#fbf9f2;
  --cream:#f5efdf;
  --hero:#ece2c8;
  --forest-a:#6f7b5c;
  --forest-b:#cfd2b8;
  --lavender:#ebe6f0;
  --footer:#f1ecdd;
  --footer-bar:#e3dcc6;
}
*{box-sizing:border-box;margin:0;padding:0}
html,body{width:1200px;height:2588px;overflow:hidden}
body{position:relative;background:linear-gradient(180deg,var(--forest-b) 0,#dcdcc6 1200px,#d9d9c2 2588px);font-family:"Open Sans",sans-serif;color:var(--ink)}
.backdrop{position:absolute;left:0;top:0;width:1200px;height:1300px;background:linear-gradient(180deg,var(--forest-a) 0,#8d9676 500px,var(--forest-b) 1300px)}
.page{position:absolute;left:150px;top:0;width:900px;height:2588px;background:var(--paper)}
.abs{position:absolute}
.header{left:0;top:0;width:900px;height:88px;background:#fff}
.brand{left:0;top:18px;width:900px;text-align:center;font-family:"Lora",serif;font-size:30px;color:var(--olive)}
.brand .dot{display:inline-block;width:18px;height:18px;border-radius:50%;background:var(--green);margin-right:10px;vertical-align:middle}
.nav{left:0;top:88px;width:900px;height:46px;background:#f7f4ea;border-top:1px solid #e6e0cc;border-bottom:1px solid #e6e0cc;display:flex;justify-content:center;gap:0}
.nav a{font-size:13px;font-weight:600;letter-spacing:1px;color:var(--muted);text-decoration:none;padding:0 22px;line-height:44px}
.nav a.active{background:var(--green);color:#fff}
.hero{left:0;top:134px;width:900px;height:426px;background:linear-gradient(90deg,#e4d8bb 0,var(--hero) 45%,#f3ecda 100%)}
.hero-photo{left:40px;top:150px;width:380px;height:400px;background:radial-gradient(ellipse at 50% 55%,#5b5146 0,#9b8c74 45%,rgba(236,226,200,0) 72%)}
.mission{right:50px;top:330px;width:380px;text-align:right;font-family:"Lora",serif;font-style:italic;font-size:21px;line-height:31px;color:#7a6e58}
.welcome{left:0;top:560px;width:900px;height:600px;background:var(--cream)}
h2{font-family:"Lora",serif;font-weight:600;font-size:20px;letter-spacing:2px;text-align:center;color:var(--ink)}
.rule{width:40px;height:2px;background:var(--green);margin:10px auto 0}
.lead{font-family:"Lora",serif;font-style:italic;font-size:15px;color:var(--muted);text-align:center}
.card{width:268px;height:278px;top:752px;background:#fff;border:1px solid #e6dfc9}
.card h3{font-family:"Lora",serif;font-weight:400;font-size:23px;color:var(--olive);text-align:center;padding-top:10px;height:50px}
.card .photo{margin:0 12px;height:120px}
.card p{font-size:12px;line-height:18px;color:var(--muted);padding:14px 16px 0}
.team{left:0;top:1160px;width:900px;height:650px;background:#f8f6ee}
.portrait{width:164px;height:164px;border-radius:50%;border:5px solid #fff;box-shadow:0 0 0 1px #ddd6c0;top:1378px}
.member{width:240px;text-align:center;top:1572px}
.member h4{font-family:"Lora",serif;font-weight:400;font-size:20px;color:var(--ink)}
.member p{font-size:12px;line-height:18px;color:var(--muted);margin-top:10px}
.cert{left:26px;top:1690px;width:848px;height:96px;background:#eef0da;border:1px solid #dfe3c2}
.cert .badge{left:36px;top:16px;width:64px;height:64px;border-radius:50%;background:var(--green)}
.cert h5{left:130px;top:16px;font-size:14px;font-weight:600;color:var(--olive)}
.cert p{left:130px;top:40px;width:690px;font-size:12px;line-height:17px;color:var(--muted)}
.quotes{left:0;top:1830px;width:900px;height:300px;background:var(--lavender)}
.quotes p{left:80px;top:40px;width:740px;text-align:center;font-family:"Lora",serif;font-style:italic;font-size:14px;line-height:22px;color:#8c8698}
.quotes .more{right:80px;top:136px;font-size:12px;color:var(--olive)}
.quotes .avatar{left:410px;top:170px;width:80px;height:80px;border-radius:50%;background:linear-gradient(135deg,#d7c7bd,#a59484);border:3px solid #fff}
.quotes .name{left:0;top:262px;width:900px;text-align:center;font-size:12px;color:var(--muted)}
.small-brand{left:0;top:2178px;width:900px;text-align:center;font-family:"Lora",serif;font-size:18px;color:var(--olive)}
.small-brand .dot{display:inline-block;width:12px;height:12px;border-radius:50%;background:var(--green);margin-right:8px;vertical-align:middle}
.footer{left:0;top:2270px;width:900px;height:256px;background:var(--footer)}
.col{top:30px;width:190px}
.col h6{font-family:"Lora",serif;font-size:15px;font-weight:600;color:var(--olive);margin-bottom:12px}
.col p,.col li{font-size:12px;line-height:20px;color:var(--muted);list-style:none}
.col li svg{vertical-align:middle;margin-right:8px}
.partners{margin-top:12px;display:flex;gap:10px}
.partners span{width:38px;height:38px;background:#cfd6e4;border-radius:4px}
.legal{left:0;top:2526px;width:900px;height:62px;background:var(--footer-bar);font-size:11px;color:var(--muted);display:flex;justify-content:space-between;align-items:center;padding:0 26px}
</style>
</head>
<body>
<div class="backdrop" role="img" aria-label="Tall pine forest background photograph"></div>
<div class="page">
  <header class="abs header">
    <div class="abs brand"><span class="dot"></span>brightcore flow</div>
  </header>
  <nav class="abs nav">
    <a class="active" href="#">HOME</a><a href="#">SCHEDULE</a><a href="#">INSTRUCTORS</a><a href="#">ABOUT</a><a href="#">GALLERY</a><a href="#">CONTACT US</a>
  </nav>

  <section class="abs hero">
    <div class="abs hero-photo" role="img" aria-label="Photo of a Pilates instructor in a seated side stretch" style="left:40px;top:16px"></div>
    <p class="abs mission" style="top:196px">Our mission is to promote long-term emotional and physical health through joyful, integrated movement training</p>
  </section>

  <section class="abs welcome">
    <h2 style="margin-top:84px">A WARM WELCOME</h2>
    <div class="rule"></div>
    <p class="lead" style="margin-top:12px">BrightCore Flow Pilates and Movement Studio is a warm and inviting studio in the heart of Maple Village</p>
  </section>

  <article class="abs card" style="left:26px">
    <h3>One-On-One Sessions</h3>
    <div class="photo" role="img" aria-label="Photo of a private session on a reformer" style="background:linear-gradient(135deg,#b9a58c,#6e6a5c)"></div>
    <p>Work with a trainer at your own pace, with a plan shaped to your body, your goals and any injury history.</p>
  </article>
  <article class="abs card" style="left:316px">
    <h3>Group Reformer Classes</h3>
    <div class="photo" role="img" aria-label="Photo of a group class on reformers" style="background:linear-gradient(135deg,#c4b49a,#7b8a9a)"></div>
    <p>Small classes on the reformer build strength, balance and length with friendly cues and a lively pace.</p>
  </article>
  <article class="abs card" style="left:606px">
    <h3>Mat Classes</h3>
    <div class="photo" role="img" aria-label="Photo of a mat class stretching together" style="background:linear-gradient(135deg,#d2c2a8,#8c7f70)"></div>
    <p>Classic mat work for every level, focused on core control, breath and mobility you can feel each day.</p>
  </article>

  <section class="abs team">
    <h2 style="margin-top:74px">OUR INSTRUCTORS</h2>
    <div class="rule"></div>
    <p class="lead" style="margin-top:12px">We inspire and nurture our clients to move more freely within themselves</p>
  </section>

  <div class="abs portrait" role="img" aria-label="Portrait of instructor Lena Marsh" style="left:88px;background:linear-gradient(135deg,#e8cfa4,#b79670)"></div>
  <div class="abs portrait" role="img" aria-label="Portrait of instructor Tessa Quinn" style="left:368px;background:linear-gradient(135deg,#9fb6d2,#4d5f78)"></div>
  <div class="abs portrait" role="img" aria-label="Portrait of instructor Rosa Delgado" style="left:648px;background:linear-gradient(135deg,#d9c6b4,#5e4a3d)"></div>

  <div class="abs member" style="left:50px"><h4>Lena Marsh</h4><p>Lena has taught Pilates for over ten years and loves helping clients find ease and strength in every move.</p></div>
  <div class="abs member" style="left:330px"><h4>Tessa Quinn</h4><p>Tessa blends reformer training and rehab work to help clients recover well and keep moving with joy.</p></div>
  <div class="abs member" style="left:610px"><h4>Rosa Delgado</h4><p>Rosa brings dance and breath work to her classes, with warm energy that keeps students coming back.</p></div>

  <div class="abs cert">
    <div class="abs badge" role="img" aria-label="Green studio certification badge"></div>
    <h5 class="abs">Eco Studio Certified</h5>
    <p class="abs">We are committed to a healthy planet. Our studio uses low energy lighting, recycled materials and non-toxic cleaning products, and we reduce waste in everything we do.</p>
  </div>

  <section class="abs quotes">
    <p class="abs">"Since joining this studio my back pain is gone and I feel stronger than I have in years. The instructors are kind, skilled and truly care about each client. Every class leaves me calm, happy and ready for the week ahead. I could not recommend it more."</p>
    <span class="abs more">&raquo; Read more</span>
    <svg class="abs" style="left:352px;top:196px" width="20" height="28" viewBox="0 0 20 28"><path d="M14 4 L4 14 L14 24" fill="none" stroke="#9a93a6" stroke-width="3"/></svg>
    <div class="abs avatar" role="img" aria-label="Photo of a studio client"></div>
    <svg class="abs" style="left:528px;top:196px" width="20" height="28" viewBox="0 0 20 28"><path d="M6 4 L16 14 L6 24" fill="none" stroke="#9a93a6" stroke-width="3"/></svg>
    <span class="abs name">Maria, client</span>
  </section>

  <div class="abs small-brand"><span class="dot"></span>brightcore flow</div>

  <footer class="abs footer">
    <div class="abs col" style="left:26px">
      <h6>About Us</h6>
      <p>BrightCore Flow Pilates and Movement Studio is a warm and friendly space for all ages and levels in Maple Village.</p>
      <div class="partners"><span></span><span></span></div>
    </div>
    <div class="abs col" style="left:250px">
      <h6>Services</h6>
      <ul><li>One-on-one sessions</li><li>Group reformer classes</li><li>Mat classes</li></ul>
    </div>
    <div class="abs col" style="left:470px">
      <h6>Social</h6>
      <ul>
        <li><svg width="10" height="10"><rect width="10" height="10" fill="#9bcb3c"/></svg>Community page</li>
        <li><svg width="10" height="10"><rect width="10" height="10" fill="#9bcb3c"/></svg>Studio news</li>
        <li><svg width="10" height="10"><rect width="10" height="10" fill="#9bcb3c"/></svg>Class updates</li>
        <li><svg width="10" height="10"><rect width="10" height="10" fill="#9bcb3c"/></svg>Client reviews</li>
      </ul>
    </div>
    <div class="abs col" style="left:690px">
      <h6>Contact Us</h6>
      <ul>
        <li><svg width="10" height="12" viewBox="0 0 10 12"><path d="M5 0a4 4 0 0 1 4 4c0 3-4 8-4 8S1 7 1 4a4 4 0 0 1 4-4z" fill="#9bcb3c"/></svg>1420 Cedar Lane, Suite 3</li>
        <li><svg width="10" height="10" viewBox="0 0 10 10"><path d="M1 1h3l1 2-1.5 1a6 6 0 0 0 2.5 2.5L7 5l2 1v3C4 9 1 6 1 1z" fill="#9bcb3c"/></svg>(555) 014-2277</li>
        <li><svg width="10" height="8"><rect width="10" height="8" fill="#9bcb3c"/></svg>hello@brightcoreflow.biz</li>
        <li><svg width="10" height="10"><circle cx="5" cy="5" r="5" fill="#9bcb3c"/></svg>brightcoreflow.biz</li>
      </ul>
    </div>
  </footer>
  <div class="abs legal"><span>&copy; Copyright BrightCore Flow</span><span>Site by studio team</span></div>
</div>
</body>
</html>
```